Northgate Roofing Works Inc Business cards

Commercial and Residential Roofing contractor needs design logo and card design. Can be single or double sided but must incorporate:
Persons Name:
Persons Title:
Mailing Address: PO Box 3719
Physical Address: 58 Fenwick Lane
Ashbury, Ma. 01692
800-316-5842
508-712-5842
Fax: 508-712-5867
Cell: Person Cell number
email address
Website: WWW.northgateroofworks.com

Target Market(s)

Residential home owners and commercial building owners

Industry/Entity Type

Roofing

Contact Information for Business Card

Persons Name:
Persons Title:
Ashbury, Ma. 01692
800-316-5842
508-712-5842
Fax: 508-712-5867
Cell: Person Cell number
email address

Logo Text

Large enough to service small enough to care

Font styles to use
Serif

Colors
0355a3

Requirements
Must have
• Commercial and Residential Roofing contractor needs design logo and card design. Can be single or double sided but must incorporate:
• Persons Name:
• Persons Title:
• Mailing Address: PO Box 3719
• Physical Address: 58 Fenwick Lane
• Ashbury, Ma. 01692
• 800-316-5842
• 508-712-5842
• Fax: 508-712-5867
• Cell: Person Cell number
• email address
• Website: WWW.northgateroofworks.com
Nice to have
• ..
Should not have
• I'm looking for something different. I have had the same card for 23 years. I attached what both sides of my present card looks like.

```html
<!DOCTYPE html>
<html lang="en">
<head>
<meta charset="utf-8">
<title>Northgate Roofing Works Inc – Business Cards</title>
<link href="https://fonts.googleapis.com/css2?family=Carlito:wght@400;700&display=swap" rel="stylesheet">
<style>
  :root {
    --brand-blue: #0b55a3;
    --card-dark: #2a2a2a;
    --card-white: #ffffff;
    --backdrop: #e4e4e4;
    --text-light: #ffffff;
  }
  * { margin: 0; padding: 0; box-sizing: border-box; }
  html, body { width: 800px; height: 1200px; overflow: hidden; }
  body {
    position: relative;
    background: var(--card-white);
    font-family: "Carlito", "Calibri", sans-serif;
  }
  .backdrop {
    position: absolute; left: 0; top: 0;
    width: 800px; height: 985px;
    background: var(--backdrop);
  }
  .card { position: absolute; overflow: hidden; }

  /* Front */
  .card-front { left: 85px; top: 77px; width: 635px; height: 361px; background: var(--card-white); }
  .front-band-top { position: absolute; left: 0; top: 0; width: 100%; height: 75px; background: var(--card-dark); }
  .front-band-bottom {
    position: absolute; left: 0; bottom: 0; width: 100%; height: 76px;
    background: var(--card-dark);
    display: flex; align-items: center; justify-content: center;
    padding-top: 16px;
  }
  .front-website { color: var(--brand-blue); font-weight: 700; font-size: 27px; letter-spacing: 0.3px; }

  .wordmark {
    position: absolute; display: flex; align-items: center;
    color: var(--brand-blue); font-weight: 700; white-space: nowrap;
  }
  .wordmark-mark { display: inline-block; background: var(--brand-blue); flex: none; }
  .wordmark-front { left: 0; width: 100%; top: 155px; justify-content: center; font-size: 46px; gap: 16px; }
  .wordmark-front .wordmark-mark { width: 30px; height: 30px; }

  /* Back */
  .card-back { left: 87px; top: 520px; width: 637px; height: 364px; background: var(--card-white); }
  .back-head { position: absolute; left: 0; top: 0; width: 100%; height: 132px; }
  .wordmark-back { left: 26px; top: 50px; font-size: 25px; gap: 10px; }
  .wordmark-back .wordmark-mark { width: 18px; height: 18px; }
  .back-rule { position: absolute; left: 0; top: 132px; width: 100%; height: 6px; background: var(--brand-blue); }
  .back-body { position: absolute; left: 0; top: 138px; width: 100%; height: 226px; background: var(--card-dark); color: var(--text-light); }

  .person { position: absolute; left: 26px; top: 26px; }
  .person-name { font-size: 25px; font-weight: 700; letter-spacing: 0.5px; line-height: 1.1; }
  .person-title { font-size: 21px; font-weight: 700; line-height: 1.2; margin-top: 2px; }

  .contact-row { position: absolute; display: flex; align-items: center; font-size: 17px; font-weight: 700; }
  .contact-row svg { fill: var(--brand-blue); flex: none; }
  .row-cell { left: 24px; top: 130px; gap: 14px; }
  .row-email { left: 24px; top: 176px; gap: 14px; }

  .contact-right { position: absolute; right: 20px; display: flex; align-items: center; gap: 14px; }
  .contact-right .lines { text-align: right; font-size: 16.5px; font-weight: 700; line-height: 22px; }
  .contact-right svg { fill: var(--brand-blue); flex: none; }
  .row-address { top: 24px; }
  .row-phones { top: 95px; }
  .row-fax { top: 167px; }

  /* Standalone logo */
  .wordmark-large { left: 0; width: 100%; top: 1063px; justify-content: center; font-size: 56px; gap: 18px; }
  .wordmark-large .wordmark-mark { width: 36px; height: 36px; }
</style>
</head>
<body>
  <div class="backdrop"></div>

  <section class="card card-front" aria-label="Card front">
    <div class="front-band-top"></div>
    <div class="wordmark wordmark-front"><span class="wordmark-mark"></span>Northgate Roofing Works</div>
    <div class="front-band-bottom"><span class="front-website">www.northgateroofworks.com</span></div>
  </section>

  <section class="card card-back" aria-label="Card back">
    <div class="back-head">
      <div class="wordmark wordmark-back"><span class="wordmark-mark"></span>Northgate Roofing Works</div>
    </div>
    <div class="back-rule"></div>
    <div class="back-body">
      <div class="person">
        <div class="person-name">MARCUS DELANEY</div>
        <div class="person-title">President</div>
      </div>

      <div class="contact-row row-cell">
        <svg width="20" height="32" viewBox="0 0 20 32" aria-hidden="true"><path d="M3 0h14a3 3 0 0 1 3 3v26a3 3 0 0 1-3 3H3a3 3 0 0 1-3-3V3a3 3 0 0 1 3-3zm0 4v21h14V4zm7 23a1.6 1.6 0 1 0 0 3.2A1.6 1.6 0 0 0 10 27z"/></svg>
        <span>508-274-1093</span>
      </div>
      <div class="contact-row row-email">
        <svg width="22" height="16" viewBox="0 0 22 16" aria-hidden="true"><path d="M0 0h22v16H0zM2 2v1l9 6 9-6V2zm0 3.4V14h18V5.4l-9 6z"/></svg>
        <span>marcusd@northgateroofworks.com</span>
      </div>

      <div class="contact-right row-address">
        <div class="lines">58 Fenwick Lane PO Box 3719<br>Ashbury, Ma. 01692</div>
        <svg width="24" height="22" viewBox="0 0 24 22" aria-hidden="true"><path d="M12 0l12 11h-3v11h-6v-7h-6v7H3V11H0z"/></svg>
      </div>
      <div class="contact-right row-phones">
        <div class="lines">800-316-5842<br>508-712-5842</div>
        <svg width="24" height="20" viewBox="0 0 24 20" aria-hidden="true"><path d="M0 6c3-4 21-4 24 0v3h-6V6H6v3H0zm5 5l3-4h8l3 4v9H5zm7 2a3 3 0 1 0 0 6 3 3 0 0 0 0-6z"/></svg>
      </div>
      <div class="contact-right row-fax">
        <div class="lines">Fax: 508-712-5867</div>
        <svg width="24" height="24" viewBox="0 0 24 24" aria-hidden="true"><path d="M6 0h12v7H6zM2 8h20a2 2 0 0 1 2 2v8h-5v-4H5v4H0v-8a2 2 0 0 1 2-2zm4 7h12v9H6z"/></svg>
      </div>
    </div>
  </section>

  <div class="wordmark wordmark-large"><span class="wordmark-mark"></span>Northgate Roofing Works</div>
</body>
</html>
```